Business Card Design Project

The business card is for an educational company that provides personalised tuition to students.

The company logo is in orange and blue (as provided) and should be included in the name card design

The philosophy of the company is to make learning a comfortable experience for student as such design of the namecard should look fresh and has a bit of the 'wow' factor. Some of the namecard design that appeals to me are as uploaded under Sample Design.

The particulars that need to be provided are:
(1): Company Name (Quillmark Education)
(1): Name
(2): Educational qualifications which will appear below name
(3): Mobile number
(4): Email address
(5): Website

Industry/Entity Type

Business

Requirements
Must have
• (1): Company Logo

(2): The card background should preferably be coloured both for the front side and back.

(3): The choice of font is important as part of the selection consideration. There is no preferred font that I have selected, designer is free to choose the font that will complement their design.

```html
<!DOCTYPE html>
<html lang="en">
<head>
<meta charset="utf-8">
<title>Quillmark Education – Business Card</title>
<link rel="stylesheet" href="https://fonts.googleapis.com/css2?family=Cinzel:wght@400&family=Libre+Baskerville:wght@400;700&display=swap">
<style>
  :root {
    --card-orange: #f3a52a;
    --card-blue: #4ea6da;
    --ink-dark: #1f1a17;
    --ink-grey: #55555f;
    --brand-grey: #4a4c52;
    --mark-orange: #e4682a;
  }
  html, body {
    margin: 0;
    padding: 0;
    overflow: hidden;
    background: #ffffff;
  }
  .card {
    position: relative;
    width: 1200px;
    height: 789px;
    overflow: hidden;
    background: var(--card-orange);
  }
  .card__backdrop {
    position: absolute;
    inset: 0;
    width: 1200px;
    height: 789px;
  }
  .holder {
    position: absolute;
    left: 494px;
    top: 156px;
    margin: 0;
  }
  .holder__name {
    margin: 0;
    font-family: "Cinzel", serif;
    font-weight: 400;
    font-size: 56px;
    line-height: 64px;
    letter-spacing: 1px;
    color: var(--ink-dark);
  }
  .holder__role {
    margin: 0;
    font-family: "Libre Baskerville", serif;
    font-size: 27px;
    line-height: 40px;
    color: var(--ink-grey);
  }
  .contact {
    position: absolute;
    left: 494px;
    top: 302px;
    margin: 0;
    padding: 0;
    list-style: none;
    font-family: "Libre Baskerville", serif;
    font-size: 26px;
    line-height: 32px;
    color: var(--ink-grey);
  }
  .brand {
    position: absolute;
    left: 494px;
    top: 557px;
    display: flex;
    align-items: center;
    gap: 22px;
  }
  .brand__square {
    flex: none;
    width: 180px;
    height: 177px;
    border-radius: 10px;
    background: var(--mark-orange);
  }
  .brand__name {
    margin: 0;
    font-family: "Libre Baskerville", serif;
    font-weight: 700;
    font-size: 74px;
    line-height: 86px;
    color: var(--brand-grey);
    white-space: nowrap;
  }
</style>
</head>
<body>
<main class="card">
  <svg class="card__backdrop" viewBox="0 0 1200 789" aria-hidden="true">
    <defs>
      <filter id="paper-grain" x="0" y="0" width="100%" height="100%">
        <feTurbulence type="fractalNoise" baseFrequency="0.9" numOctaves="2" seed="4" result="grain"/>
        <feColorMatrix in="grain" type="matrix" values="0 0 0 0 0  0 0 0 0 0  0 0 0 0 0  0 0 0 0.18 0"/>
      </filter>
    </defs>
    <path class="card__sky" fill="var(--card-blue)"
          d="M0 0 H663 C 500 55, 350 190, 275 360 C 200 530, 80 650, 0 712 Z"/>
    <rect width="1200" height="789" filter="url(#paper-grain)"/>
  </svg>

  <header class="holder">
    <h1 class="holder__name">Daniel R. Hartley</h1>
    <p class="holder__role">College Student</p>
  </header>

  <ul class="contact">
    <li class="contact__phone">1-555-014-276800</li>
    <li class="contact__email">drhartley@postmail.com</li>
    <li class="contact__web">www.drhartley.com</li>
  </ul>

  <div class="brand">
    <div class="brand__square"></div>
    <p class="brand__name">Quillmark<br>Education</p>
  </div>
</main>
</body>
</html>
```